Redesign Business Cards, Attached

Please read instructions carefully. If you have any questions send a message before submitting your ONE design. Please redesign attached business cards. Double sided. Use same content and descriptions. Use black, silver, crimson red and gold colors. My only issue with the attached design is the background colors. I like the layout as-is. I can provide the individual pictures on the back side later. Do not submit more than one design. One submission shall include both front and back. Do not submit front and back separately. A second project will be launched to create a matching post card after completion of this.
Industry/Entity Type
see description and attachments.
Contact Information for Business Card
Requirements
Must have
- see description and attachments.
Nice to have
Should not have

```html
<!DOCTYPE html>
<html lang="en">
<head>
<meta charset="utf-8">
<title>Harborline Boat Training &amp; Charters — Business Card</title>
<link href="https://fonts.googleapis.com/css2?family=Montserrat:wght@400;700&family=Ubuntu:wght@400;500&display=swap" rel="stylesheet">
<style>
  :root {
    --black: #151515;
    --tile-black: #1c1c1e;
    --pill-black: #111111;
    --crimson: #b22024;
    --gold: #fcc853;
    --name-gold: #f2b927;
    --silver: #d0d0d0;
    --silver-dark: #a9a9ad;
    --white: #ffffff;
    --backdrop: #2f3033;
  }
  html, body {
    margin: 0;
    width: 1200px;
    height: 1200px;
    overflow: hidden;
    background: var(--backdrop);
  }
  .sheet {
    position: relative;
    width: 1200px;
    height: 1200px;
  }
  .card {
    position: absolute;
    left: 110px;
    width: 980px;
    height: 560px;
    display: block;
    box-shadow: 0 10px 30px rgba(0,0,0,.45);
  }
  .card--front { top: 30px; }
  .card--back { top: 610px; }

  .fill-black { fill: var(--black); }
  .fill-gold { fill: var(--gold); }
  .fill-silver { fill: var(--silver); }
  .fill-silver-dark { fill: var(--silver-dark); }
  .fill-white { fill: var(--white); }

  .red-panel { fill: var(--crimson); stroke: var(--white); stroke-width: 7; stroke-linejoin: miter; }
  .photo-frame { fill: none; stroke: var(--silver); stroke-width: 10; }

  .holder-name { font-family: 'Montserrat', sans-serif; font-weight: 700; font-size: 31px; fill: var(--name-gold); letter-spacing: 1px; }
  .holder-title { font-family: 'Montserrat', sans-serif; font-weight: 400; font-size: 25px; fill: var(--white); }
  .phone-pill { fill: var(--pill-black); }
  .phone-text { font-family: 'Montserrat', sans-serif; font-weight: 700; font-size: 24px; fill: var(--white); }
  .contact-text { font-family: 'Montserrat', sans-serif; font-weight: 400; font-size: 24px; fill: var(--white); }
  .contact-icon { fill: none; stroke: var(--gold); stroke-width: 2.4; }

  .brand-name { font-family: 'Montserrat', sans-serif; font-weight: 700; fill: var(--black); text-anchor: middle; }

  .tile--black { fill: var(--tile-black); }
  .tile--crimson { fill: var(--crimson); }
  .tile-label { font-family: 'Ubuntu', sans-serif; font-weight: 500; font-size: 21px; fill: var(--white); text-anchor: middle; }
</style>
</head>
<body>
<main class="sheet">

  <!-- Front side -->
  <svg class="card card--front" viewBox="0 0 980 560" aria-label="Business card front">
    <defs>
      <clipPath id="gold-bands">
        <rect x="0" y="0" width="980" height="110"/>
        <rect x="0" y="430" width="980" height="130"/>
      </clipPath>
    </defs>
    <rect class="fill-black" x="0" y="0" width="980" height="560"/>
    <polygon class="fill-gold" clip-path="url(#gold-bands)" points="490,0 980,0 980,560 560,560 372,258"/>
    <polygon class="red-panel" points="578,0 985,0 985,565 647,565 450,258"/>

    <g class="brand-badge">
      <circle class="fill-white" cx="200" cy="268" r="155"/>
      <text class="brand-name" x="200" y="262" font-size="34">HARBORLINE</text>
      <text class="brand-name" x="200" y="296" font-size="15">BOAT TRAINING &amp; CHARTERS</text>
    </g>

    <g class="holder">
      <text class="holder-name" x="560" y="140">DALTON R. WHITMORE</text>
      <text class="holder-title" x="585" y="182">USCG Licensed Captain</text>
      <text class="holder-title" x="610" y="218">Certified Instructor</text>

      <rect class="phone-pill" x="582" y="250" width="308" height="44" rx="22"/>
      <text class="phone-text" x="602" y="281">TEXT (555) 014-2876</text>

      <g class="contact contact--email">
        <rect class="contact-icon" x="620" y="318" width="28" height="19"/>
        <polyline class="contact-icon" points="620,318 634,330 648,318"/>
        <text class="contact-text" x="662" y="337">hello@helmready.com</text>
      </g>
      <g class="contact contact--web">
        <circle class="contact-icon" cx="634" cy="370" r="13"/>
        <ellipse class="contact-icon" cx="634" cy="370" rx="6" ry="13"/>
        <line class="contact-icon" x1="621" y1="370" x2="647" y2="370"/>
        <text class="contact-text" x="662" y="379">www.HelmReady.com</text>
      </g>
    </g>
  </svg>

  <!-- Back side -->
  <svg class="card card--back" viewBox="0 0 980 560" aria-label="Business card back">
    <defs>
      <linearGradient id="sea" x1="0" y1="0" x2="1" y2="1">
        <stop offset="0" stop-color="#cfe7f5"/>
        <stop offset="0.45" stop-color="#5f93b8"/>
        <stop offset="1" stop-color="#1f4f78"/>
      </linearGradient>
    </defs>
    <rect class="fill-silver" x="0" y="0" width="980" height="560"/>
    <polygon class="fill-black" points="0,0 520,0 451,112 490,193 0,302"/>
    <polygon class="fill-gold" points="480,0 520,0 500,40 470,28"/>
    <polygon class="photo-frame" points="520,0 980,0 980,252 490,193 451,112"/>
    <polygon role="img" aria-label="Photo of a white motor yacht cruising across sparkling open water" fill="url(#sea)" points="520,0 980,0 980,252 490,193 451,112"/>

    <g class="brand-badge">
      <circle class="fill-white" cx="245" cy="101" r="92"/>
      <text class="brand-name" x="245" y="100" font-size="21">HARBORLINE</text>
      <text class="brand-name" x="245" y="122" font-size="9.5">BOAT TRAINING &amp; CHARTERS</text>
    </g>

    <g class="services">
      <rect class="tile--black" x="128" y="232" width="172" height="112"/>
      <text class="tile-label" x="214" y="268">Hands-On<tspan x="214" dy="24">Boat</tspan><tspan x="214" dy="24">Training</tspan></text>

      <rect class="tile--crimson" x="90" y="352" width="172" height="112"/>
      <text class="tile-label" x="176" y="402">Island<tspan x="176" dy="24">Anchoring</tspan></text>

      <rect class="tile--crimson" x="308" y="212" width="172" height="112"/>
      <text class="tile-label" x="394" y="248">Introduction<tspan x="394" dy="24">to Power</tspan><tspan x="394" dy="24">boating</tspan></text>

      <rect class="tile--black" x="282" y="332" width="172" height="112"/>
      <text class="tile-label" x="368" y="368">Open Water<tspan x="368" dy="24">Advanced</tspan><tspan x="368" dy="24">Maneuvers</tspan></text>

      <rect class="tile--black" x="488" y="196" width="172" height="112"/>
      <text class="tile-label" x="574" y="232">Precision<tspan x="574" dy="24">Docking &amp;</tspan><tspan x="574" dy="24">Boat Handling</tspan></text>

      <rect class="tile--crimson" x="462" y="316" width="172" height="112"/>
      <text class="tile-label" x="548" y="366">Coastal<tspan x="548" dy="24">Navigation</tspan></text>

      <rect class="tile--crimson" x="668" y="180" width="172" height="112"/>
      <text class="tile-label" x="754" y="216">Open Water<tspan x="754" dy="24">Boat</tspan><tspan x="754" dy="24">Handling</tspan></text>

      <rect class="tile--black" x="642" y="300" width="182" height="112"/>
      <text class="tile-label" x="733" y="336" font-size="19">Captaining/<tspan x="733" dy="24">Piloting Service</tspan><tspan x="733" dy="24">for Your Outings</tspan></text>
    </g>
  </svg>

</main>
</body>
</html>
```